The Harvest Compass

Cutting Through the Noise to What Actually Works.

Nutrition book

Target Market(s)

People looking to be or get healthy and eat right.

```html
<!DOCTYPE html>
<html lang="en">
<head>
<meta charset="utf-8">
<title>The Harvest Compass – Book Design</title>
<link href="https://fonts.googleapis.com/css2?family=Montserrat:wght@500;700;800;900&family=Playfair+Display:wght@500;700&family=Source+Sans+3:wght@400;600&display=swap" rel="stylesheet">
<style>
:root{
  --bg:#e9eaec;
  --paper:#ffffff;
  --cover-blue:#1f6fb5;
  --cover-blue-dark:#0f4d8a;
  --cover-sky:#4fa3dd;
  --yellow:#ffd21f;
  --ink:#2b2f36;
  --ink-soft:#5d636c;
  --red:#d93a2b;
  --blue:#2b6cc4;
  --green:#4d9a2e;
  --orange:#ee8a1d;
  --purple:#7b3fa6;
  --slate:#3f4a57;
  --page-blue:#e4f0f8;
  --page-yellow:#faf3b8;
  --gold:#c9a24a;
}
*{margin:0;padding:0;box-sizing:border-box}
html,body{width:1200px;height:997px;overflow:hidden;background:var(--bg)}
body{position:relative;font-family:"Source Sans 3",sans-serif;color:var(--ink)}
.sheet{position:absolute;background:var(--paper);box-shadow:0 6px 18px rgba(0,0,0,.14)}
.spread{display:flex}
.page{position:relative;width:50%;height:100%;overflow:hidden}
.page+.page{border-left:1px solid #d9dcdf}
.art{position:absolute;border-radius:10px}
p.body{font-size:11.5px;line-height:1.45;color:var(--ink-soft)}

/* cover */
.cover{left:40px;top:28px;width:400px;height:484px;overflow:hidden}
.cover-sky{position:absolute;inset:0 0 auto 0;height:300px;background:linear-gradient(160deg,var(--cover-blue-dark),var(--cover-blue) 55%,var(--cover-sky));clip-path:polygon(0 0,100% 0,100% 78%,0 100%)}
.cover-side{position:absolute;top:40px;width:22px;height:300px;background:linear-gradient(180deg,#f1c24a,#e86b3a 50%,#7bb447)}
.cover-side.left{left:0}.cover-side.right{right:0}
.cover-title{position:absolute;top:28px;left:0;right:0;text-align:center;font-family:"Montserrat",sans-serif;font-weight:900;font-size:40px;line-height:1;color:#fff;letter-spacing:.5px}
.cover-title .accent{display:block;color:var(--yellow);font-size:42px}
.cover-sub{position:absolute;top:124px;left:40px;right:40px;text-align:center;font-family:"Montserrat",sans-serif;font-weight:700;font-size:17px;line-height:1.15;color:var(--yellow)}
.stack{position:absolute;display:flex;flex-direction:column;gap:4px}
.layer{height:var(--h,30px);border-radius:4px;color:#fff;font-family:"Montserrat",sans-serif;font-weight:800;text-transform:uppercase;display:flex;align-items:center;gap:8px;padding-left:10px;box-shadow:0 4px 0 rgba(0,0,0,.25)}
.layer .dot{width:16px;height:16px;border-radius:50%;background:rgba(255,255,255,.85);flex:none}
.l-cal{background:var(--red)}.l-pro{background:var(--blue)}.l-fq{background:var(--green)}
.l-mt{background:var(--orange)}.l-sup{background:var(--purple)}.l-noise{background:var(--slate)}
.cover .stack{left:70px;top:196px;width:270px}
.cover .layer{--h:30px;font-size:17px}
.cover .layer:nth-child(2){margin-left:8px}.cover .layer:nth-child(3){margin-left:-4px}
.cover .layer:nth-child(4){margin-left:6px}.cover .layer:nth-child(5){margin-left:2px}.cover .layer:nth-child(6){margin-left:8px}
.author-photo{position:absolute;left:30px;top:406px;width:62px;height:62px;border-radius:50%;background:linear-gradient(135deg,#c9d7e6,#8ea9c4);border:3px solid #fff;box-shadow:0 0 0 2px var(--gold)}
.author-name{position:absolute;left:106px;top:412px;font-family:"Playfair Display",serif;font-weight:700;font-size:24px;color:var(--gold);text-transform:uppercase}
.author-role{position:absolute;left:112px;top:446px;font-family:"Montserrat",sans-serif;font-weight:700;font-size:10px;letter-spacing:1px;color:var(--ink-soft)}

/* spread: layers */
.spread-layers{left:480px;top:28px;width:690px;height:484px}
.page-blue{background:var(--page-blue)}
.h-sans{font-family:"Montserrat",sans-serif;font-weight:800;color:var(--ink)}
.spread-layers .page-blue .h-sans{position:absolute;left:30px;top:44px;font-size:25px}
.spread-layers .page-blue p.body{position:absolute;left:30px;top:86px;right:26px}
.spread-layers .stack{left:30px;top:170px;width:230px}
.spread-layers .layer{--h:32px;font-size:16px}
.spread-layers .layer:nth-child(even){margin-left:6px}
.callouts{position:absolute;left:262px;top:178px;display:flex;flex-direction:column;gap:16px}
.callout{display:flex;align-items:center;gap:6px}
.callout i{display:block;width:22px;height:1px;background:var(--ink-soft)}
.callout b{display:block;width:20px;height:20px;border-radius:50%;background:#fff;border:2px solid var(--ink-soft)}
.needs .h-sans{position:absolute;left:26px;font-size:17px}
.needs .h1{top:20px}.needs .h2{top:262px}
.needs p.body{position:absolute;left:26px;width:190px}
.needs .p1{top:50px}.needs .p2{top:292px}
.art-almond{right:16px;top:96px;width:110px;height:110px;background:radial-gradient(circle,#c79a6b,#8c5f38 60%,#6e8d3a)}
.art-wheat{right:16px;top:330px;width:100px;height:120px;background:linear-gradient(180deg,#e7c98f,#b88a4a)}

/* spread: intro */
.spread-intro{left:30px;top:540px;width:690px;height:430px}
.intro .h-serif{position:absolute;left:30px;top:32px;font-family:"Playfair Display",serif;font-weight:500;font-size:26px}
.intro p.body{position:absolute;left:30px;top:80px;right:26px}
.dropcap{float:left;font-family:"Playfair Display",serif;font-size:44px;line-height:.9;margin:2px 6px 0 0;color:var(--ink)}
.art-fish{left:26px;top:220px;width:190px;height:190px;background:linear-gradient(135deg,#b6c4cf,#e49a7a 55%,#8fa3b3)}
.art-broc{left:228px;top:250px;width:86px;height:86px;border-radius:50%;background:radial-gradient(circle,#6fae3c,#2f7a2a)}
.page-yellow{background:var(--page-yellow)}
.steps-title{position:absolute;left:0;right:0;top:58px;text-align:center;font-family:"Playfair Display",serif;font-weight:500;font-size:27px;letter-spacing:1px;text-transform:uppercase}
.steps-icon{position:absolute;left:50%;top:18px;margin-left:-16px}
.steps{position:absolute;left:22px;right:22px;top:110px;list-style:none;display:flex;flex-direction:column;gap:14px}
.step{display:flex;gap:12px}
.step svg{flex:none;margin-top:18px}
.step h3{font-family:"Playfair Display",serif;font-weight:700;font-size:16px}
.step p.body{font-size:11px}

/* single page */
.page-single{left:760px;top:540px;width:400px;height:430px}
.art-body{left:90px;top:24px;width:220px;height:210px;background:radial-gradient(ellipse at center,#f3e3c4,#d9ecd2 60%,#ffffff)}
.art-family{left:30px;top:240px;width:340px;height:170px;background:linear-gradient(180deg,#f2d6bd,#d8a074 60%,#a9c8a0)}
</style>
</head>
<body>

<section class="sheet cover" aria-label="Book cover">
  <div class="cover-sky"></div>
  <div class="cover-side left" role="img" aria-label="Strip of fresh fruit and vegetables"></div>
  <div class="cover-side right" role="img" aria-label="Strip of fresh salmon and greens"></div>
  <h1 class="cover-title">THE HARVEST <span class="accent">COMPASS</span></h1>
  <p class="cover-sub">Cutting Through the Noise to What Actually Works.</p>
  <div class="stack">
    <div class="layer l-cal"><span class="dot"></span>Calories</div>
    <div class="layer l-pro"><span class="dot"></span>Protein</div>
    <div class="layer l-fq"><span class="dot"></span>Food Quality</div>
    <div class="layer l-mt"><span class="dot"></span>Meal Timing</div>
    <div class="layer l-sup"><span class="dot"></span>Supplements</div>
    <div class="layer l-noise"><span class="dot"></span>Noise</div>
  </div>
  <div class="author-photo" role="img" aria-label="Author portrait"></div>
  <div class="author-name">Dr. Maren Holloway</div>
  <div class="author-role">AUTHOR &amp; DIETITIAN | RESEARCHER</div>
</section>

<section class="sheet spread spread-layers" aria-label="Spread: the logic of the layers">
  <div class="page page-blue">
    <h2 class="h-sans">The Logic of the Layers</h2>
    <p class="body">Each layer in this model builds on the one beneath it, so start at the base and move upward only once the foundation feels steady and simple to keep.</p>
    <div class="stack">
      <div class="layer l-cal"><span class="dot"></span>Calories</div>
      <div class="layer l-pro"><span class="dot"></span>Protein</div>
      <div class="layer l-fq"><span class="dot"></span>Food Quality</div>
      <div class="layer l-mt"><span class="dot"></span>Meal Timing</div>
      <div class="layer l-sup"><span class="dot"></span>Supplements</div>
      <div class="layer l-noise"><span class="dot"></span>Noise</div>
    </div>
    <div class="callouts">
      <div class="callout"><i></i><b></b></div>
      <div class="callout"><i></i><b></b></div>
      <div class="callout"><i></i><b></b></div>
      <div class="callout"><i></i><b></b></div>
      <div class="callout"><i></i><b></b></div>
      <div class="callout"><i></i><b></b></div>
    </div>
  </div>
  <div class="page needs">
    <h2 class="h-sans h1">Understanding Your Needs</h2>
    <p class="body p1">Your body needs vary with age, activity, sleep and stress. Learn what your daily energy use looks like, then match intake to it. Small honest notes on what you eat reveal patterns faster than any app or trend ever will.</p>
    <div class="art art-almond" role="img" aria-label="Illustration of almonds and leaves"></div>
    <h2 class="h-sans h2">Making Informed Choices</h2>
    <p class="body p2">Read labels with calm curiosity. Favour foods with short ingredient lists, plenty of fibre and enough protein. Treat bold claims on the front of a package as marketing, not as guidance, and trust the numbers printed on the back.</p>
    <div class="art art-wheat" role="img" aria-label="Illustration of wheat stalks and grains"></div>
  </div>
</section>

<section class="sheet spread spread-intro" aria-label="Spread: introduction and actionable steps">
  <div class="page intro">
    <h2 class="h-serif">Introduction</h2>
    <p class="body"><span class="dropcap">A</span> world of diet advice competes for your attention every day. This book sorts it into a clear order of importance, so you can spend your effort where it truly pays off and quietly ignore the rest.</p>
    <div class="art art-fish" role="img" aria-label="Illustration of a salmon"></div>
    <div class="art art-broc" role="img" aria-label="Illustration of broccoli"></div>
  </div>
  <div class="page page-yellow">
    <svg class="steps-icon" width="32" height="32" viewBox="0 0 32 32" fill="none" stroke="#2b2f36" stroke-width="1.6"><path d="M4 18h24a12 10 0 0 1-24 0z"/><path d="M12 12c0-3 3-3 3-6M18 12c0-3 3-3 3-6"/></svg>
    <h2 class="steps-title">Actionable Steps</h2>
    <ul class="steps">
      <li class="step">
        <svg width="26" height="26" viewBox="0 0 26 26" fill="none" stroke="#2b2f36" stroke-width="1.8"><circle cx="13" cy="13" r="11"/><path d="M13 7v6l4 3"/></svg>
        <div><h3>Set Your Baseline</h3><p class="body">Track what you eat for one week to find your true starting point.</p></div>
      </li>
      <li class="step">
        <svg width="26" height="26" viewBox="0 0 26 26" fill="none" stroke="#2b2f36" stroke-width="1.8"><rect x="5" y="3" width="16" height="20" rx="2"/><path d="M9 9l2 2 4-4M9 16h8"/></svg>
        <div><h3>Choose Whole Foods</h3><p class="body">Build most meals around foods with one ingredient and little processing.</p></div>
      </li>
      <li class="step">
        <svg width="26" height="26" viewBox="0 0 26 26" fill="none" stroke="#2b2f36" stroke-width="1.8"><rect x="3" y="4" width="20" height="19" rx="3"/><path d="M9 12a4 4 0 0 1 8 0M13 12l2-2"/></svg>
        <div><h3>Choose Variety</h3><p class="body">Rotate colours, grains and proteins across the week for broader nutrients.</p></div>
      </li>
      <li class="step">
        <svg width="26" height="26" viewBox="0 0 26 26" fill="none" stroke="#2b2f36" stroke-width="1.8"><path d="M2 4h4l3 12h12l2-8H8"/><circle cx="11" cy="21" r="1.6"/><circle cx="19" cy="21" r="1.6"/></svg>
        <div><h3>Matching Your Foods</h3><p class="body">Pair each plate with your goals and plan the shopping list around it.</p></div>
      </li>
    </ul>
  </div>
</section>

<section class="sheet page-single" aria-label="Illustrated page">
  <div class="art art-body" role="img" aria-label="Illustration of a human figure filled with foods, surrounded by food icons"></div>
  <div class="art art-family" role="img" aria-label="Illustration of a family sharing a healthy meal at the table"></div>
</section>

</body>
</html>
```